" é uma corretora de seguros, onde trabalharei com todos os ramos: seguro de automovel, vida, seguro viagem, residencia, condominio, transportes, carga... previdencia e tambem com consorcio. "

```html
<!DOCTYPE html>
<html lang="pt-BR">
<head>
<meta charset="utf-8">
<title>Assinatura de e-mail – Rota Seguros</title>
<link href="https://fonts.googleapis.com/css2?family=Open+Sans:wght@400;600&display=swap" rel="stylesheet">
<style>
  :root {
    --page-bg: #ebe8e4;
    --card-white: #ffffff;
    --brand-blue: #1d6a9e;
    --text-on-blue: #ffffff;
  }
  * { margin: 0; padding: 0; box-sizing: border-box; }
  html, body {
    width: 1200px;
    height: 1200px;
    overflow: hidden;
    background: var(--page-bg);
    font-family: "Open Sans", Arial, sans-serif;
  }
  .signature {
    position: absolute;
    left: 173px;
    top: 461px;
    width: 854px;
    height: 278px;
    filter: drop-shadow(0 6px 14px rgba(0,0,0,0.18));
  }
  .signature__shape {
    position: absolute;
    inset: 0;
  }
  .brand {
    position: absolute;
    left: 34px;
    top: 62px;
    display: flex;
    align-items: center;
    gap: 16px;
    height: 88px;
  }
  .brand__square {
    width: 88px;
    height: 88px;
    background: var(--brand-blue);
  }
  .brand__name {
    color: var(--brand-blue);
    font-size: 34px;
    font-weight: 600;
    letter-spacing: -0.5px;
    white-space: nowrap;
  }
  .contact {
    position: absolute;
    left: 446px;
    top: 22px;
    color: var(--text-on-blue);
  }
  .contact__name {
    font-size: 34px;
    font-weight: 600;
    line-height: 1.1;
    margin-bottom: 12px;
  }
  .contact__line {
    display: flex;
    align-items: center;
    gap: 10px;
    font-size: 20px;
    line-height: 1;
    height: 32px;
  }
  .contact__icon {
    width: 18px;
    height: 18px;
    flex: none;
  }
  .contact__address {
    margin-top: 30px;
    font-size: 14.5px;
    line-height: 1.65;
  }
</style>
</head>
<body>
  <div class="signature">
    <svg class="signature__shape" viewBox="0 0 854 278" width="854" height="278" aria-hidden="true">
      <path d="M0 0 H854 V278 H36 A36 36 0 0 1 0 242 Z" fill="var(--card-white)"/>
      <path d="M418 0 H818 A36 36 0 0 1 854 36 V278 H372 Q404 170 418 0 Z" fill="var(--brand-blue)"/>
    </svg>

    <div class="brand">
      <div class="brand__square"></div>
      <span class="brand__name">Rota Seguros</span>
    </div>

    <div class="contact">
      <p class="contact__name">Helena Prado</p>
      <p class="contact__line">
        <svg class="contact__icon" viewBox="0 0 18 18" aria-hidden="true">
          <circle cx="9" cy="9" r="9" fill="#fff"/>
          <path d="M6 4.5c.5-.3 1 0 1.2.4l.7 1.5c.2.4 0 .8-.3 1l-.6.5c.5 1.1 1.4 2 2.5 2.5l.5-.6c.3-.3.7-.4 1-.3l1.5.7c.4.2.6.7.4 1.2-.4.9-1.2 1.4-2.1 1.2C8 12.2 5.8 10 5.4 7.2c-.2-1 .2-2.2.6-2.7z" fill="var(--brand-blue)"/>
        </svg>
        11 97654.3210
      </p>
      <p class="contact__line">
        <svg class="contact__icon" viewBox="0 0 18 18" aria-hidden="true">
          <circle cx="9" cy="9" r="9" fill="#fff"/>
          <circle cx="9" cy="9" r="2.2" fill="none" stroke="var(--brand-blue)" stroke-width="1.5"/>
          <path d="M11.2 7.2v2.6c0 1 1.5 1.2 1.8 0 .6-2.6-1.2-5-4-5a4.2 4.2 0 1 0 2.3 7.7" fill="none" stroke="var(--brand-blue)" stroke-width="1.5" stroke-linecap="round"/>
        </svg>
        helena@rotaseguros.com.br
      </p>
      <p class="contact__address">
        Rua das Acácias, 210 Centro - Campinas / SP - Tel. 19 3232.7788<br>
        www.rotaseguros.com.br
      </p>
    </div>
  </div>
</body>
</html>
```